International Business Consulting Company Website

RV Crestline Advisory is a U.S-based international consulting firm. We combined passion for success in the global business arena with hands-on experience to help foreign companies navigate the entry into U.S. markets and U.S. companies in initiating and expanding exports to foreign markets.

We need a simple 1 page website
Examples of other consultants’ websites:
http://www.falconridgeadvisors.example/#intro
https://www.mtq-advisers.example
http://veronagroup.example
https://harborwiseadvisory.example

I also need the designer to suggest stock images that are suitable (related to international business, exports).

We want our web design to be bold, yet clean and simple.

Target Market(s)

US companies that export abroad, foreign companies that want to do business int he US/ open a subsidiary in the US.

Industry/Entity Type

Business Consultant

Coding

Coded - Design and coding required

Font styles to use
Sans Serif

Requirements
Must have
• Company logo on top

```html
<!DOCTYPE html>
<html lang="en">
<head>
<meta charset="utf-8">
<title>RV Crestline Advisory</title>
<link rel="stylesheet" href="https://fonts.googleapis.com/css2?family=Nunito+Sans:wght@400;600;700;800&display=swap">
<style>
:root{
  --backdrop:#efefef;
  --page:#ffffff;
  --brand:#1f4fa0;
  --ink:#333333;
  --muted:#555555;
  --hero-deep:#1e3f82;
  --hero-mid:#3d63a8;
}
*{margin:0;padding:0;box-sizing:border-box}
html,body{width:1200px;height:1200px;overflow:hidden;background:var(--backdrop)}
body{font-family:"Nunito Sans",sans-serif;color:var(--ink);position:relative}
.page{position:absolute;left:318px;top:14px;width:564px;height:1167px;background:var(--page)}
.abs{position:absolute}
.logo{left:36px;top:8px;display:flex;align-items:center;gap:5px;color:var(--brand);font-weight:700;font-size:12px;letter-spacing:.2px}
.logo-square{width:16px;height:16px;border:1.5px solid var(--brand)}
.nav{right:36px;top:13px;display:flex;gap:22px;font-size:5.6px;letter-spacing:.3px;color:var(--muted)}
.hero{left:36px;width:493px;overflow:hidden}
.hero-one{top:30px;height:182px;background:linear-gradient(160deg,var(--hero-mid) 0%,var(--hero-deep) 55%,#2c4f93 100%)}
.hero-two{top:574px;height:181px;background:linear-gradient(180deg,#8fa6c9 0%,#5f7fb0 35%,#3e5f95 70%,#2f4d80 100%)}
.hero-title{position:absolute;left:34px;color:#fff;font-weight:700;letter-spacing:.5px;line-height:1}
.hero-tag{position:absolute;background:#fff;color:var(--brand);font-weight:700;line-height:1;padding:1px 2px 0}
.hero-one .hero-title{top:56px;font-size:39px}
.hero-one .hero-tag{left:36px;top:95px;font-size:24.5px}
.hero-two .hero-title{top:52px;font-size:36px}
.hero-two .hero-tag{left:34px;top:90px;font-size:24px}
.section-title{width:564px;text-align:center;font-size:7.4px;font-weight:600;letter-spacing:.3px;color:var(--ink)}
.intro{left:80px;width:404px;text-align:center;font-size:5.5px;line-height:8.8px;color:var(--muted)}
.intro strong{display:block;font-size:6.2px;color:var(--ink);margin-bottom:1px}
.portrait{left:247px;top:298px;width:71px;height:71px;border-radius:50%;border:2px solid #888;background:radial-gradient(circle at 50% 40%,#8a7264 0%,#3b302b 60%,#1c1a1a 100%)}
.about-col{width:197px;font-size:5.4px;line-height:8.8px;color:var(--muted);text-align:justify}
.about-col p{margin-bottom:8.8px}
.svc-col{font-size:5.4px;color:var(--muted)}
.svc-lead{font-size:6.8px;line-height:8.8px;margin-bottom:9px;width:200px}
.svc-lead b{color:var(--ink);font-weight:700}
.svc-list{list-style:none}
.svc-list li{position:relative;padding-left:6px;line-height:8.8px}
.svc-list li::before{content:"";position:absolute;left:0;top:3.4px;width:2px;height:2px;border-radius:50%;background:var(--ink)}
.contact{left:36px;top:926px;width:493px;height:201px;background:linear-gradient(180deg,#7a6a86 0%,#8c6c78 40%,#a67e6e 75%,#6b5566 100%)}
.contact-card{position:absolute;left:156px;top:42px;width:181px;height:116px;background:rgba(240,240,242,.9);text-align:center;color:var(--muted)}
.contact-card h3{margin-top:25px;font-size:7.2px;font-weight:600;letter-spacing:.3px;color:var(--ink)}
.card-company{margin-top:3px;font-size:6.4px}
.card-name{margin-top:2px;font-size:5.5px;color:var(--ink)}
.card-name b{font-weight:700}
.card-role{font-size:4.8px;font-style:italic;line-height:5px}
.card-line{display:flex;justify-content:center;align-items:center;gap:5px;font-size:5.4px;line-height:8.8px}
.card-line svg{width:6px;height:6px;fill:#444}
.card-lines{margin-top:11px}
.footer{left:36px;top:1144px;font-size:5.2px;color:var(--muted)}
</style>
</head>
<body>
<div class="page">
  <header>
    <div class="abs logo"><span class="logo-square"></span>RV Crestline Advisory</div>
    <nav class="abs nav"><span>HOME</span><span>ABOUT</span><span>SERVICES</span><span>CONTACT</span></nav>
  </header>

  <section class="abs hero hero-one" role="img" aria-label="Blue-toned night photo of a city skyline and bridge over a river">
    <h1 class="hero-title">WE COMBINED</h1>
    <div class="hero-tag">PASSION FOR SUCCESS</div>
  </section>

  <h2 class="abs section-title" style="top:236px">WELCOME TO RV CRESTLINE ADVISORY</h2>
  <div class="abs intro" style="top:251px">
    <strong>RV Crestline Advisory is a U.S-based international consulting firm.</strong>
    We combined passion for success in the global business arena with hands-on experience to help foreign companies navigate the entry into U.S. markets and U.S. companies in initiating and expanding exports to foreign markets.
  </div>

  <div class="abs portrait" role="img" aria-label="Portrait photo of the company president"></div>
  <h2 class="abs section-title" style="top:381px">ABOUT</h2>

  <div class="abs about-col" style="left:71px;top:403px">
    <p>Mira Danek has ten years of experience in economic development, foreign direct investment (FDI) and trade. Prior to founding RV Crestline Advisory, she worked as Director of Global Business Development – Europe at the State Economic Development Commission (SEDC) assisting European companies to expand in the state. While at the SEDC, Mira participated in a number of international trade shows and organized multiple investment and trade missions for the state's governors.</p>
    <p>Mira was appointed by the U.S. Secretary of Commerce to the Regional District Export Council (RDEC), an organization of business leaders whose expertise in international business provides a source of professional advice for the region's firms. She was elected to serve as the RDEC Vice Chair in 2017. Mira is a speaker at the Export Academy, an RDEC program providing export training and education. She will teach an International Business Management class at the Central State University during the fall semester of 2017.</p>
  </div>
  <div class="abs about-col" style="left:298px;top:403px">
    <p>Mira serves as the first ever Czech Honorary Consul for the State. With her strong network on both sides of the Atlantic, Mira supports bilateral economic and trade relations between the Czech Republic, the European Union and the United States.</p>
    <p>Passionate about her community, Mira has joined several non-profit boards and organizations, including the Riverside Cancer Institute Foundation Fund Board, the Global Policy Institute, the Civic Club, the Women's Leadership Forum, the Network of Women in Global Trade, and the Scholars Alumni Board.</p>
    <p>Mira is a 2005 honors MBA graduate of the Central State University. She obtained her undergraduate BA degree in finance and international business from the same institution. She is a member of the Leadership State Class XI and the Leadership Metro Class XXVI.</p>
    <p>Mira is fluent in English and Czech. She also speaks German and Slovakian.</p>
  </div>

  <section class="abs hero hero-two" role="img" aria-label="Aerial photo of a dense city skyline under a cloudy sky">
    <h2 class="hero-title">USA MARKET ENTRY</h2>
    <div class="hero-tag">AND EXPANDING EXPORTS</div>
  </section>

  <h2 class="abs section-title" style="top:775px">OUR SERVICES</h2>
  <div class="abs svc-col" style="left:71px;top:798px">
    <p class="svc-lead"><b>RV Crestline Advisory – Exports</b> assists U.S. companies with their export initiatives by</p>
    <ul class="svc-list">
      <li>Identifying and developing new customer relationships in foreign markets</li>
      <li>Organizing trade mission trips</li>
      <li>Coordinating successful trade show visits</li>
      <li>Providing an assistance with the completion of a strategic export plan</li>
      <li>Finding additional resources to support and grow companies' exports</li>
      <li>Connecting companies with other international trade experts to further<br>support their international logistics, payment &amp; financing management,<br>and to address any trade regulations and legal issues</li>
    </ul>
  </div>
  <div class="abs svc-col" style="left:301px;top:798px">
    <p class="svc-lead"><b>RV Crestline Advisory – FDI</b> assists international companies with navigating the entry into U.S. markets by</p>
    <ul class="svc-list">
      <li>Managing the site selection process</li>
      <li>Collecting market data</li>
      <li>Site identification and analysis</li>
      <li>Providing an appraisal of proposed incentives and financing assistance</li>
    </ul>
  </div>

  <section class="abs contact" role="img" aria-label="Hazy sunset photo of a city skyline beside a river">
    <div class="contact-card">
      <h3>CONTACT US HERE</h3>
      <p class="card-company">RV Crestline Advisory, LLC</p>
      <p class="card-name"><b>Mira Danek,</b> MBA</p>
      <p class="card-role">President</p>
      <div class="card-lines">
        <p class="card-line"><svg viewBox="0 0 10 10"><path d="M0 2h10v6H0z M0 2l5 3.5L10 2" stroke="#f0f0f2" stroke-width=".8"/></svg>info@rvcrestline.example</p>
        <p class="card-line"><svg viewBox="0 0 10 10"><path d="M2 0.5l2 2-1 1.3c.6 1.3 1.6 2.4 2.9 3l1.3-1 2 2-1.2 1.6C4.5 9.2.6 5.4.5 1.6z"/></svg>+1 (555) 014-0192</p>
      </div>
    </div>
  </section>

  <footer class="abs footer">© 2017 RV Crestline Advisory. All Rights Reserved.</footer>
</div>
</body>
</html>
```